Stonebell Inc Ad Design, trying to attract new customers

Please see attached pictures and files for information
We are a Class A - Residential General Contractor in Lynchburg, VA with Master HVAC and Master PLUMBING Licenses. We focus on Water and Air Solutions for property owners.
We build, remodel, and repair homes
We do HVAC, including Humidity Control and Air Purification
We do Plumbing
We love to fix Water Leaks for Plumbing, Roof Leaks, Skylight Leaks, Basement Leaks, Foundation Leaks, Door and Window Leaks
We solve water and air issues on the outside of properties with custom structures, grading, and landscaping

Target Market(s)

Residential and Light Commercial property owners

Industry/Entity Type

Construction

Font styles to use
Other font styles liked:
• see cards

Colors
0054AA
0677BA
7BADD7
CADEEF
E8F1F8
00AB8E
00BBA5
67D7C9
C6EFE9
E9F9F6

Requirements
Must have
• See business cards
Nice to have
• see business cards
Should not have
• My name

```html
<!DOCTYPE html>
<html lang="en">
<head>
<meta charset="utf-8">
<title>Stonebell Inc – Water and Air Solutions</title>
<link rel="stylesheet" href="https://fonts.googleapis.com/css2?family=Anton&family=Roboto+Condensed:wght@500;700&family=Arimo:wght@400&display=swap">
<style>
  :root {
    --stage: #9a9a9a;
    --paper: #ffffff;
    --navy: #0b5a92;
    --band: #1a75bd;
    --band-light: #0aa3e3;
    --green: #1f7a3c;
    --leaf-dark: #1b7f3a;
    --leaf-light: #8cc63f;
    --ink: #161616;
    --rule: #1a6fb4;
  }
  * { box-sizing: border-box; margin: 0; padding: 0; }
  html, body { width: 1200px; height: 744px; overflow: hidden; }
  body { background: var(--stage); position: relative; }

  .ad {
    position: absolute; left: 124px; top: 124px;
    width: 952px; height: 496px;
    background: var(--paper);
    box-shadow: 14px 14px 14px rgba(0,0,0,.35);
    overflow: hidden;
  }
  .ad-art { position: absolute; left: 0; top: 0; width: 952px; height: 496px; }

  .headline {
    position: absolute; left: 0; width: 952px;
    font-family: "Anton", "Oswald", sans-serif;
    color: var(--navy);
    text-align: center;
    line-height: 1;
    letter-spacing: .5px;
    text-shadow: -2px 0 #fff, 2px 0 #fff, 0 -2px #fff, 0 2px #fff,
                 -1.5px -1.5px #fff, 1.5px 1.5px #fff, -1.5px 1.5px #fff, 1.5px -1.5px #fff;
  }
  .headline--slogan { top: 22px; font-size: 51px; padding-left: 78px; }
  .headline--licence { top: 87px; font-size: 51px; padding-left: 80px; }

  .brand {
    position: absolute; left: 26px; top: 266px;
    display: flex; align-items: center; gap: 7px;
    font-family: "Roboto Condensed", sans-serif; font-weight: 700;
    font-size: 22px; color: var(--navy); letter-spacing: 1.5px;
  }
  .brand-dot { width: 14px; height: 14px; border-radius: 50%; background: var(--navy); }

  .contact {
    position: absolute; right: 360px; text-align: right;
    font-family: "Roboto Condensed", sans-serif; font-weight: 500;
    color: var(--green); white-space: nowrap;
  }
  .contact--phone {
    top: 210px; font-family: "Anton", sans-serif; font-weight: 400;
    font-size: 43px; color: var(--navy); letter-spacing: 1px; line-height: 1;
  }
  .contact--email { top: 262px; font-size: 19px; }
  .contact--web { top: 302px; font-size: 24px; }
  .contact--licence { top: 331px; font-size: 24px; }

  .divider {
    position: absolute; left: 618px; top: 196px;
    width: 2px; height: 182px; background: var(--rule);
  }

  .services {
    position: absolute; left: 643px; top: 200px;
    list-style: none;
    font-family: "Arimo", Arial, sans-serif; font-size: 16px;
    color: var(--ink); line-height: 21.1px;
  }
  .services li::before { content: "-"; display: inline-block; width: 14px; }

  .scripture {
    position: absolute; left: 25px; color: #fff;
    font-family: "Arimo", Arial, sans-serif;
  }
  .scripture-ref { top: 383px; font-size: 15px; }
  .scripture-text { top: 417px; width: 900px; font-size: 15.4px; line-height: 18.4px; }
</style>
</head>
<body>
  <main class="ad">
    <svg class="ad-art" viewBox="0 0 952 496" aria-hidden="false">
      <defs>
        <linearGradient id="canopy" x1="0" y1="0" x2="0" y2="1">
          <stop offset="0" stop-color="var(--leaf-light)"/>
          <stop offset="1" stop-color="var(--leaf-dark)"/>
        </linearGradient>
        <linearGradient id="bandFill" x1="0" y1="0" x2="1" y2="0">
          <stop offset="0" stop-color="var(--band)"/>
          <stop offset=".35" stop-color="var(--band-light)"/>
          <stop offset=".6" stop-color="var(--band)"/>
          <stop offset="1" stop-color="var(--band)"/>
        </linearGradient>
      </defs>
      <rect role="img" aria-label="Illustration of a large green tree whose trunk turns into a winding blue river"
            x="0" y="0" width="420" height="206" rx="60" fill="url(#canopy)"/>
      <path d="M0 367 C 120 330, 260 388, 417 399 L 952 399 L 952 496 L 0 496 Z" fill="url(#bandFill)"/>
    </svg>

    <h1 class="headline headline--slogan">“WE PUT WATER AND AIR IN ITS PLACE”</h1>
    <p class="headline headline--licence">CLASS A RBC PLUMBING HVAC</p>

    <div class="brand"><span class="brand-dot"></span>STONEBELL</div>

    <p class="contact contact--phone">(434) 555-0187</p>
    <p class="contact contact--email">contact@StonebellVA.com</p>
    <p class="contact contact--web">www.ShadeBuiltVA.com</p>
    <p class="contact contact--licence">Licensed and Insured</p>

    <div class="divider"></div>

    <ul class="services">
      <li>Humidity Control/Air Purificatin</li>
      <li>Roof/Skylight Leaks</li>
      <li>Basement/Foundation Leaks</li>
      <li>Drainage/Grading/Landscaping</li>
      <li>Custom Outdoor Structures - Porches</li>
      <li>Decks</li>
      <li>Sunrooms</li>
      <li>Gazebos</li>
    </ul>

    <p class="scripture scripture-ref">PSALM 1:1-3</p>
    <p class="scripture scripture-text">Blessed is the man who walks not in the counsel of the ungodly, nor stands in the path of sinners, nor sits in the seat of the scornful; but his delight is in the law of the Lord, and in His law he meditates day and night. He shall be like a tree planted by the rivers of water, that brings forth fruit in it’s season, whose leaf shall not wither, and whatever he does shall prosper.</p>
  </main>
</body>
</html>
```